Varnel blockchain

A Blockchain investment company template for a switzerland based company. The company is also offering its own blockchain infrastructure in partnership with a top 200 blockchain project, on which blockchain startups can develop their ideas.
In addition, co-working spaces are offered in an innovation center.
So these three parts should be covered in the template

1. Crypto investment
2. Offering the blockchain infrastructure
3. Co-working spaces (https://moravent.example/)

Target Market(s)

Blockchain / Crypto

Colors
ec1f27

Requirements
Must have
• Connection to the three parts mentioned in the description
inculding to logo attached
Nice to have
• connection to switzerland

```html
<!DOCTYPE html>
<html lang="en">
<head>
<meta charset="utf-8">
<title>Varnel Blockchain – Presentation Template</title>
<link href="https://fonts.googleapis.com/css2?family=Work+Sans:wght@500;600;700&family=Poppins:wght@400;500;600&family=Roboto:wght@400;500;700&display=swap" rel="stylesheet">
<style>
:root{
  --red:#ec1f27;
  --red-deep:#8a0a12;
  --ink:#1c1c1c;
  --muted:#3a3a3a;
  --board:#474c51;
  --paper:#ffffff;
  --night:#140406;
  --grey-bar:#c9c9c9;
}
*{box-sizing:border-box;margin:0;padding:0}
html,body{width:1200px;height:3839px;overflow:hidden;background:var(--board)}
body{position:relative;font-family:'Poppins',sans-serif;color:var(--ink)}
.slide{position:absolute;left:80px;width:1040px;height:585px;background:var(--paper);overflow:hidden}
.s-cover{top:49px}
.s-invest{top:680px}
.s-infra{top:1310px}
.s-intro{top:1941px;background:var(--night)}
.s-cowork{top:2573px}
.s-thanks{top:3203px}

/* header bar */
.topbar{position:absolute;left:0;top:0;width:100%;height:52px;border-bottom:2px solid var(--red);display:flex;align-items:center;justify-content:space-between;padding:0 27px}
.brand{font-family:'Roboto',sans-serif;font-weight:700;font-size:23px;letter-spacing:-0.6px;color:var(--red)}
.topbar-tag{font-family:'Work Sans',sans-serif;font-weight:500;font-size:15px;color:var(--ink)}
.s-intro .topbar{border-bottom-color:rgba(255,255,255,.75)}
.s-intro .brand,.s-intro .topbar-tag{color:#fff}

/* cover */
.cover-art{position:absolute;inset:0;background:
  radial-gradient(ellipse 70% 45% at 50% 92%,#f3a0a6 0%,#d8323c 25%,rgba(160,12,22,.6) 55%,transparent 80%),
  linear-gradient(180deg,#3d0308 0%,#7c0911 55%,#a3101a 100%)}
.cover-name{position:absolute;left:0;right:0;top:255px;text-align:center;font-family:'Roboto',sans-serif;font-weight:700;font-size:62px;letter-spacing:-1.8px;color:#fff}

/* text blocks */
.copy{position:absolute;left:52px;width:430px}
.h-title{font-family:'Work Sans',sans-serif;font-weight:600;font-size:35px;line-height:1.15;color:var(--ink)}
.h-sub{font-family:'Work Sans',sans-serif;font-weight:600;font-size:20px;line-height:26px;color:var(--ink);margin-top:10px}
.body-text{font-size:12.5px;line-height:24px;color:var(--muted);margin-top:18px}
.s-intro .h-title,.s-intro .h-sub{color:#fff}
.s-intro .body-text{color:#f2e6e7}

.bullets{list-style:none;margin-top:20px}
.bullets li{display:flex;gap:14px;align-items:flex-start;height:46.5px;font-size:12px;line-height:16px;color:var(--muted)}
.bullets svg{flex:none;margin-top:-1px}

.photo{position:absolute;border-radius:0}
.photo-invest{left:544px;top:109px;width:450px;height:410px;background:linear-gradient(135deg,#5d4a3c 0%,#2d2a2c 45%,#7a5530 80%,#a26b2c 100%)}
.photo-intro{left:470px;top:0;width:570px;height:585px;background:
  radial-gradient(ellipse 55% 30% at 45% 78%,rgba(236,31,39,.85),transparent 70%),
  radial-gradient(ellipse 40% 60% at 75% 30%,rgba(200,20,30,.55),transparent 70%),
  linear-gradient(90deg,var(--night) 0%,#3a060b 60%,#4d0810 100%)}
.s-intro .topbar,.s-intro .copy{z-index:2}

/* infrastructure */
.infra-head{position:absolute;left:0;right:0;top:100px;text-align:center}
.infra-head .h-title{font-size:27px}
.infra-head p{width:840px;margin:12px auto 0;font-size:13.5px;line-height:23px;color:var(--muted)}
.timeline{position:absolute;left:107px;top:365px;width:823px;border-top:2px dotted #b5b5b5}
.step{position:absolute;top:220px;width:150px;margin-left:-75px;text-align:center}
.step-badge{display:block;margin:0 auto}
.step-dot{position:absolute;left:66px;top:139px;width:18px;height:18px;border:2px solid var(--red);border-radius:50%;background:#fff}
.step-dot::after{content:"";position:absolute;left:4px;top:4px;width:6px;height:6px;border-radius:50%;background:var(--red)}
.step-stem{position:absolute;left:74px;top:158px;height:42px;border-left:2px dotted #b5b5b5}
.step h3{margin-top:84px;font-size:12px;font-weight:600;color:var(--ink)}
.step p{margin-top:6px;font-size:10.5px;line-height:15px;color:var(--muted)}

/* chart */
.chart{position:absolute;left:544px;top:128px;width:449px;height:356px;border:2px solid #d4d4d4;border-radius:3px;background:#fff}
.chart text{font-family:'Poppins',sans-serif;font-size:10px;fill:#555}

/* thank you */
.thanks-title{position:absolute;left:52px;top:40px;font-family:'Roboto',sans-serif;font-weight:700;font-size:32px;letter-spacing:.5px;color:var(--ink)}
.thanks-rule{position:absolute;left:0;right:0;top:93px;border-top:2px solid var(--red)}
.contact{position:absolute;display:flex;align-items:center;gap:14px;font-family:'Roboto',sans-serif;font-size:19px;color:var(--ink)}
.contact svg{flex:none}
.skyline{position:absolute;left:0;right:0;bottom:0;height:362px;background:linear-gradient(180deg,rgba(255,255,255,0) 0%,rgba(236,31,39,.35) 30%,rgba(236,31,39,.75) 70%,var(--red) 100%)}
</style>
</head>
<body>

<!-- Cover -->
<section class="slide s-cover">
  <div class="cover-art" role="img" aria-label="Glowing red network globe of connected nodes over a deep red background"></div>
  <h1 class="cover-name">Varnel Blockchain</h1>
</section>

<!-- Crypto investment -->
<section class="slide s-invest">
  <header class="topbar"><span class="brand">Varnel Blockchain</span><span class="topbar-tag">Crypto Investment</span></header>
  <div class="copy" style="top:100px">
    <h2 class="h-title">Crypto investment</h2>
    <p class="h-sub">Sed ut perspiciatis unde omnis iste natus voluptatem accusantium doloremque laudantium, totam</p>
    <ul class="bullets">
      <li><svg width="22" height="22" viewBox="0 0 22 22"><circle cx="11" cy="11" r="11" fill="#ec1f27"/><path d="M6 11h9M11 7l4 4-4 4" stroke="#fff" stroke-width="2" fill="none" stroke-linecap="round" stroke-linejoin="round"/></svg><span>Nemo enim ipsam voluptatem quia voluptas sit aspernatur aut odit aut fugit, sed quia consequuntur magni dolores</span></li>
      <li><svg width="22" height="22" viewBox="0 0 22 22"><circle cx="11" cy="11" r="11" fill="#ec1f27"/><path d="M6 11h9M11 7l4 4-4 4" stroke="#fff" stroke-width="2" fill="none" stroke-linecap="round" stroke-linejoin="round"/></svg><span>Nemo enim ipsam voluptatem quia voluptas sit aspernatur aut odit aut fugit, sed quia consequuntur magni dolores</span></li>
      <li><svg width="22" height="22" viewBox="0 0 22 22"><circle cx="11" cy="11" r="11" fill="#ec1f27"/><path d="M6 11h9M11 7l4 4-4 4" stroke="#fff" stroke-width="2" fill="none" stroke-linecap="round" stroke-linejoin="round"/></svg><span>Nemo enim ipsam voluptatem quia voluptas sit aspernatur aut odit aut fugit, sed quia consequuntur magni dolores</span></li>
      <li><svg width="22" height="22" viewBox="0 0 22 22"><circle cx="11" cy="11" r="11" fill="#ec1f27"/><path d="M6 11h9M11 7l4 4-4 4" stroke="#fff" stroke-width="2" fill="none" stroke-linecap="round" stroke-linejoin="round"/></svg><span>Nemo enim ipsam voluptatem quia voluptas sit aspernatur aut odit aut fugit, sed quia consequuntur magni dolores</span></li>
      <li><svg width="22" height="22" viewBox="0 0 22 22"><circle cx="11" cy="11" r="11" fill="#ec1f27"/><path d="M6 11h9M11 7l4 4-4 4" stroke="#fff" stroke-width="2" fill="none" stroke-linecap="round" stroke-linejoin="round"/></svg><span>Nemo enim ipsam voluptatem quia voluptas sit aspernatur aut odit aut fugit, sed quia consequuntur magni dolores</span></li>
      <li><svg width="22" height="22" viewBox="0 0 22 22"><circle cx="11" cy="11" r="11" fill="#ec1f27"/><path d="M6 11h9M11 7l4 4-4 4" stroke="#fff" stroke-width="2" fill="none" stroke-linecap="round" stroke-linejoin="round"/></svg><span>Nemo enim ipsam voluptatem quia voluptas sit aspernatur aut odit aut fugit, sed quia consequuntur magni dolores</span></li>
    </ul>
  </div>
  <div class="photo photo-invest" role="img" aria-label="Photo of a laptop showing a crypto trading chart on a café table, a drink beside it"></div>
</section>

<!-- Blockchain infrastructure -->
<section class="slide s-infra">
  <header class="topbar"><span class="brand">Varnel Blockchain</span><span class="topbar-tag">Offering the blockchain infrastructure</span></header>
  <div class="infra-head">
    <h2 class="h-title">Offering the blockchain infrastructure</h2>
    <p>Sed ut perspiciatis unde omnis iste natus error sit voluptatem accusantium doloremque laudantium, totam rem aperiam, eaque ipsa quae ab illo inventore veritatis et quasi architecto beatae vitae dicta sunt explicabo.</p>
  </div>
  <div class="timeline"></div>

  <div class="step" style="left:107px">
    <svg class="step-badge" width="112" height="122" viewBox="0 0 112 122"><path d="M56 122l-14-14h28z" fill="#ec1f27"/><circle cx="56" cy="56" r="56" fill="#ec1f27"/><circle cx="56" cy="56" r="41" fill="#fff"/>
      <g fill="none" stroke="#222" stroke-width="2"><rect x="38" y="38" width="12" height="12"/><rect x="62" y="38" width="12" height="12"/><rect x="38" y="62" width="12" height="12"/><rect x="62" y="62" width="12" height="12"/><path d="M50 44h12M50 68h12M44 50v12M68 50v12"/></g></svg>
    <span class="step-dot"></span><span class="step-stem"></span>
    <h3>Nemo enim ipsam</h3>
    <p>Sed ut perspiciatis unde omnis iste natus error sit voluptatem accusantium doloremque laudantium, totam rem aperiam, eaque ipsa</p>
  </div>
  <div class="step" style="left:271px">
    <svg class="step-badge" width="112" height="122" viewBox="0 0 112 122"><path d="M56 122l-14-14h28z" fill="#ec1f27"/><circle cx="56" cy="56" r="56" fill="#ec1f27"/><circle cx="56" cy="56" r="41" fill="#fff"/>
      <g fill="none" stroke="#222" stroke-width="2"><rect x="36" y="38" width="34" height="9"/><rect x="36" y="50" width="34" height="9"/><rect x="36" y="62" width="28" height="9"/><path d="M70 60l8 3v7c0 5-4 8-8 10-4-2-8-5-8-10v-7z"/></g></svg>
    <span class="step-dot"></span><span class="step-stem"></span>
    <h3>Nemo enim ipsam</h3>
    <p>Sed ut perspiciatis unde omnis iste natus error sit voluptatem accusantium doloremque laudantium, totam rem aperiam, eaque ipsa</p>
  </div>
  <div class="step" style="left:437px">
    <svg class="step-badge" width="112" height="122" viewBox="0 0 112 122"><path d="M56 122l-14-14h28z" fill="#ec1f27"/><circle cx="56" cy="56" r="56" fill="#ec1f27"/><circle cx="56" cy="56" r="41" fill="#fff"/>
      <g fill="none" stroke="#222" stroke-width="2"><rect x="38" y="38" width="36" height="12" rx="6"/><rect x="38" y="62" width="14" height="12"/><rect x="60" y="62" width="14" height="12"/><path d="M41 62v-5a4 4 0 018 0v5M63 62v-5a4 4 0 018 0v5"/></g></svg>
    <span class="step-dot"></span><span class="step-stem"></span>
    <h3>Nemo enim ipsam</h3>
    <p>Sed ut perspiciatis unde omnis iste natus error sit voluptatem accusantium doloremque laudantium, totam rem aperiam, eaque ipsa</p>
  </div>
  <div class="step" style="left:601px">
    <svg class="step-badge" width="112" height="122" viewBox="0 0 112 122"><path d="M56 122l-14-14h28z" fill="#ec1f27"/><circle cx="56" cy="56" r="56" fill="#ec1f27"/><circle cx="56" cy="56" r="41" fill="#fff"/>
      <g fill="none" stroke="#222" stroke-width="2"><circle cx="56" cy="37" r="4"/><circle cx="38" cy="52" r="4"/><circle cx="74" cy="52" r="4"/><circle cx="45" cy="73" r="4"/><circle cx="67" cy="73" r="4"/><circle cx="56" cy="56" r="4"/><path d="M56 41v11M42 52h10M60 56h10M53 59l-6 11M59 59l6 11M49 73h14M54 40l-14 9M58 40l14 9"/></g></svg>
    <span class="step-dot"></span><span class="step-stem"></span>
    <h3>Nemo enim ipsam</h3>
    <p>Sed ut perspiciatis unde omnis iste natus error sit voluptatem accusantium doloremque laudantium, totam rem aperiam, eaque ipsa</p>
  </div>
  <div class="step" style="left:766px">
    <svg class="step-badge" width="112" height="122" viewBox="0 0 112 122"><path d="M56 122l-14-14h28z" fill="#ec1f27"/><circle cx="56" cy="56" r="56" fill="#ec1f27"/><circle cx="56" cy="56" r="41" fill="#fff"/>
      <g fill="none" stroke="#222" stroke-width="2" stroke-linejoin="round"><path d="M56 34l10 5v11l-10 5-10-5V39zM46 39l10 5 10-5M56 44v11"/><path d="M44 57l10 5v11l-10 5-10-5V62zM34 62l10 5 10-5M44 67v11"/><path d="M68 57l10 5v11l-10 5-10-5V62zM58 62l10 5 10-5M68 67v11"/></g></svg>
    <span class="step-dot"></span><span class="step-stem"></span>
    <h3>Nemo enim ipsam</h3>
    <p>Sed ut perspiciatis unde omnis iste natus error sit voluptatem accusantium doloremque laudantium, totam rem aperiam, eaque ipsa</p>
  </div>
  <div class="step" style="left:930px">
    <svg class="step-badge" width="112" height="122" viewBox="0 0 112 122"><path d="M56 122l-14-14h28z" fill="#ec1f27"/><circle cx="56" cy="56" r="56" fill="#ec1f27"/><circle cx="56" cy="56" r="41" fill="#fff"/>
      <g fill="none" stroke="#222" stroke-width="2"><circle cx="56" cy="56" r="11"/><circle cx="56" cy="34" r="3"/><circle cx="56" cy="78" r="3"/><circle cx="34" cy="56" r="3"/><circle cx="78" cy="56" r="3"/><circle cx="40" cy="40" r="3"/><circle cx="72" cy="40" r="3"/><circle cx="40" cy="72" r="3"/><circle cx="72" cy="72" r="3"/><path d="M56 37v8M56 67v8M37 56h8M67 56h8M42 42l6 6M70 42l-6 6M42 70l6-6M70 70l-6-6"/></g>
      <text x="56" y="61" text-anchor="middle" font-family="Poppins,sans-serif" font-size="14" font-weight="600" fill="#222">$</text></svg>
    <span class="step-dot"></span><span class="step-stem"></span>
    <h3>Nemo enim ipsam</h3>
    <p>Sed ut perspiciatis unde omnis iste natus error sit voluptatem accusantium doloremque laudantium, totam rem aperiam, eaque ipsa</p>
  </div>
</section>

<!-- Introduction -->
<section class="slide s-intro">
  <div class="photo photo-intro" role="img" aria-label="Red digital padlock of glowing polygon lines under falling binary code"></div>
  <header class="topbar"><span class="brand">Varnel Blockchain</span><span class="topbar-tag">Introduction</span></header>
  <div class="copy" style="top:126px">
    <h2 class="h-title">Welcome To<br>Varnel Blockchain</h2>
    <p class="h-sub" style="margin-top:14px">Sed ut perspiciatis unde omnis iste natus voluptatem accusantium doloremque laudantium, totam</p>
    <p class="body-text">Sed ut perspiciatis unde omnis iste natus error sit voluptatem accusantium doloremque laudantium, totam rem aperiam, eaque ipsa quae ab illo inventore veritatis et quasi architecto beatae vitae dicta sunt explicabo. Nemo enim ipsam voluptatem quia voluptas sit aspernatur aut odit aut fugit, sed quia consequuntur magni dolores eos qui ratione voluptatem sequi nesciunt. Neque porro quisquam est, qui dolorem ipsum quia dolor sit amet, consectetur, adipisci velit, sed quia non numquam eius modi tempora incidunt ut labore et</p>
  </div>
</section>

<!-- Co-working spaces -->
<section class="slide s-cowork">
  <header class="topbar"><span class="brand">Varnel Blockchain</span><span class="topbar-tag">Co-working spaces</span></header>
  <div class="copy" style="top:126px">
    <h2 class="h-title">Co-working spaces</h2>
    <p class="h-sub">Sed ut perspiciatis unde omnis iste natus voluptatem accusantium doloremque laudantium, totam</p>
    <p class="body-text">Sed ut perspiciatis unde omnis iste natus error sit voluptatem accusantium doloremque laudantium, totam rem aperiam, eaque ipsa quae ab illo inventore veritatis et quasi architecto beatae vitae dicta sunt explicabo. Nemo enim ipsam voluptatem quia voluptas sit aspernatur aut odit aut fugit, sed quia consequuntur magni dolores eos qui ratione voluptatem sequi nesciunt. Neque porro quisquam est, qui dolorem ipsum quia dolor sit amet, consectetur, adipisci velit, sed quia non numquam eius modi tempora incidunt ut labore et dolore magnam aliquam quaerat voluptatem. Ut enim ad minima</p>
  </div>
  <div class="chart">
    <svg width="445" height="352" viewBox="0 0 445 352">
      <g stroke="#e3e3e3" stroke-width="1">
        <line x1="50" y1="30" x2="430" y2="30"/><line x1="50" y1="69" x2="430" y2="69"/><line x1="50" y1="107" x2="430" y2="107"/><line x1="50" y1="146" x2="430" y2="146"/><line x1="50" y1="184" x2="430" y2="184"/><line x1="50" y1="223" x2="430" y2="223"/><line x1="50" y1="261" x2="430" y2="261"/>
      </g>
      <line x1="50" y1="26" x2="50" y2="300" stroke="#888"/><line x1="50" y1="300" x2="430" y2="300" stroke="#888"/>
      <g text-anchor="end">
        <text x="40" y="33">35K</text><text x="40" y="72">30K</text><text x="40" y="110">25K</text><text x="40" y="149">20K</text><text x="40" y="187">15K</text><text x="40" y="226">10K</text><text x="40" y="264">5K</text><text x="40" y="303">0</text>
      </g>
      <g fill="var(--red)">
        <rect x="62" y="123" width="15" height="177"/><rect x="116" y="84" width="15" height="216"/><rect x="171" y="84" width="15" height="216"/><rect x="225" y="53" width="15" height="247"/><rect x="279" y="96" width="15" height="204"/><rect x="334" y="76" width="15" height="224"/><rect x="388" y="45" width="15" height="255"/>
      </g>
      <g fill="var(--grey-bar)">
        <rect x="78" y="146" width="15" height="154"/><rect x="132" y="115" width="15" height="185"/><rect x="187" y="157" width="15" height="143"/><rect x="241" y="115" width="15" height="185"/><rect x="295" y="180" width="15" height="120"/><rect x="350" y="165" width="15" height="135"/><rect x="404" y="153" width="15" height="147"/>
      </g>
      <g text-anchor="middle">
        <text x="77" y="320">Mon</text><text x="131" y="320">Tue</text><text x="186" y="320">Wed</text><text x="240" y="320">Thu</text><text x="294" y="320">Fri</text><text x="349" y="320">Sat</text><text x="403" y="320">Sun</text>
      </g>
    </svg>
  </div>
</section>

<!-- Thank you -->
<section class="slide s-thanks">
  <h2 class="thanks-title">THANK YOU</h2>
  <div class="thanks-rule"></div>
  <div class="contact" style="left:52px;top:136px">
    <svg width="20" height="20" viewBox="0 0 24 24"><path fill="#ec1f27" d="M6.6 10.8a15.1 15.1 0 006.6 6.6l2.2-2.2c.3-.3.7-.4 1-.2 1.1.4 2.3.6 3.6.6.6 0 1 .4 1 1V20c0 .6-.4 1-1 1A17 17 0 013 4c0-.6.4-1 1-1h3.5c.6 0 1 .4 1 1 0 1.3.2 2.5.6 3.6.1.3 0 .7-.2 1z"/></svg>
    <span>+1 555 0142 7730</span>
  </div>
  <div class="contact" style="left:467px;top:136px">
    <svg width="22" height="18" viewBox="0 0 22 18"><rect x="0" y="1" width="22" height="16" rx="2" fill="#ec1f27"/><path d="M1 3l10 7 10-7" stroke="#fff" stroke-width="1.6" fill="none"/></svg>
    <span>info@varnelblockchain.example</span>
  </div>
  <div class="contact" style="left:52px;top:183px">
    <svg width="20" height="20" viewBox="0 0 20 20"><g fill="none" stroke="#ec1f27" stroke-width="2"><circle cx="10" cy="10" r="8.5"/><ellipse cx="10" cy="10" rx="3.5" ry="8.5"/><path d="M1.5 10h17M3 5.5h14M3 14.5h14"/></g></svg>
    <span>www.varnelblockchain.example</span>
  </div>
  <div class="contact" style="left:469px;top:183px">
    <svg width="18" height="22" viewBox="0 0 18 22"><path fill="#ec1f27" d="M9 0a8 8 0 018 8c0 6-8 14-8 14S1 14 1 8a8 8 0 018-8zm0 5a3 3 0 100 6 3 3 0 000-6z"/></svg>
    <span>4345 enim ipsam voluptatem quia voluptas</span>
  </div>
  <div class="skyline" role="img" aria-label="Red city skyline of tall buildings with patterned windows"></div>
</section>

</body>
</html>
```